Design and put together a 5 page A4 brochure for a Training Programme

Carrowmere Institute of Training deliver a Nationally Accredited Programme in Medical Reception and Administration.

We have a new Qualification (Cert III Business Administration) and we require a 5 page brochure to be designed. (I have CHANGED THIS TO 5 Pages as I can see it is too crowded and not clean enough)

I would put a 6th page in as an application form.

We have recently rebranded our website which is currently under development - so a .jpg will be available of the 'look and feel of this'. I will also upload some stock photos which could be used in the design.

This is an important project for us - so your fantastic work will be greatly appreciated.

This project is fairly urgent - so it is likely we will be choosing a 'winner' to work with sooner rather than later.

Thanks for considering!

I will be uploading various graphics/drafts now.
Updates

Target Market(s)

1/ Women 25-45 yrs undertaking studies in being a medical receptionist
2/ Medical Practices who are hiring Trainees for their medical clinic or hospital

Industry/Entity Type

Medical

Font styles to use
Serif
Sans Serif

Colors
0455a3
fbe7d2
f68e4e
fef4ee
3176b5
33a6d7
f37122

Requirements
Must have
• Clear and clean design - professional
• Graphics of medical pictures (I will supply some so you get the look and feel of wht we are looking for)
• Corporate branding (I will upload a .jpg of new website design for look and feel
• The colour I would like with blue is also a STONE colour - I could not find it in the colour wheel on this site.
• The partner logos should be on the last page probably in one faded colour (such as grey)
Should not have
• I must be able to see the inside of the brochure also, I can not pick this purely on the front cover. Thanks :-)
• I have also now updated the Company Logo

```html
<!DOCTYPE html>
<html lang="en">
<head>
<meta charset="utf-8">
<title>Carrowmere Institute of Training – Certificate III Brochure</title>
<link rel="stylesheet" href="https://fonts.googleapis.com/css2?family=Yanone+Kaffeesatz:wght@400;500&family=Marcellus+SC&family=Open+Sans:wght@400;600;700&display=swap">
<style>
:root{
  --navy:#2e4466;
  --navy-deep:#263a59;
  --sky:#2a9fd6;
  --sky-soft:#8cc6e8;
  --ice:#e4f2fa;
  --ice-2:#cfe7f5;
  --paper:#ffffff;
  --ink:#3a4656;
  --stage:#dde3ea;
}
*{box-sizing:border-box;margin:0;padding:0}
html,body{width:1200px;height:1200px;overflow:hidden;background:var(--stage)}
body{position:relative;font-family:"Open Sans",Arial,sans-serif;color:var(--ink)}
.page{position:absolute;background:var(--paper);overflow:hidden;box-shadow:0 4px 14px rgba(20,35,60,.25)}
.page--top{top:76px;width:326px;height:456px}
.page--bottom{top:631px;width:332px;height:462px}
.cover{left:215px}
.intro{left:654px}
.course{left:66px}
.package{left:444px}
.funding{left:815px}
.abs{position:absolute}
.photo{position:absolute}
.tiny{font-size:4.6px;line-height:1.42}
.hd{position:absolute;background:var(--navy);color:#fff;font-family:"Marcellus SC",Georgia,serif;font-size:9px;letter-spacing:.3px;padding:2px 22px 1px 10px;clip-path:polygon(0 0,100% 0,calc(100% - 10px) 100%,0 100%)}
.hd--small{font-size:7.4px;padding:2px 18px 1px 12px}
.brand{font-family:"Marcellus SC",Georgia,serif;color:var(--navy);display:flex;align-items:center;gap:4px}
.brand__dot{width:9px;height:9px;background:var(--navy)}
.tick li{list-style:none;padding-left:7px;position:relative}
.tick li::before{content:"";position:absolute;left:0;top:1.5px;width:3px;height:1.6px;border-left:.8px solid var(--sky);border-bottom:.8px solid var(--sky);transform:rotate(-45deg)}
.dots li{list-style:none;padding-left:6px;position:relative}
.dots li::before{content:"";position:absolute;left:0;top:2px;width:2.4px;height:2.4px;border-radius:50%;background:var(--sky)}
b{font-weight:700}

/* cover */
.cover__band-text{position:absolute;left:218px;top:4px;transform-origin:0 0;transform:rotate(61deg);font-family:"Open Sans",sans-serif;font-size:9.6px;color:#fff;white-space:nowrap}
.cover__name{position:absolute;left:0;top:343px;width:222px;height:24px;background:var(--sky-soft);font-family:"Yanone Kaffeesatz",sans-serif;font-size:17px;color:var(--navy);padding:2px 0 0 10px}
.cover__contact{position:absolute;left:14px;top:380px;color:#fff;font-size:9px}
.cover__contact .phone{font-size:13px;margin-top:3px}
.cover__tag{position:absolute;right:14px;top:402px;text-align:right;font-family:"Marcellus SC",Georgia,serif;color:var(--navy);font-size:15.5px;line-height:1.15}

/* intro */
.intro__box{position:absolute;left:13px;top:9px;width:301px;height:264px;background:var(--navy);border-radius:5px}
.intro__code{position:absolute;left:18px;top:72px;width:110px;text-align:center;font-family:"Yanone Kaffeesatz",sans-serif;color:#fff;font-size:17px;line-height:1.25}
.intro__code .code{color:var(--sky);font-size:21px;font-weight:500;line-height:1.1}
.intro__body{position:absolute;left:135px;top:17px;width:170px;color:#e7eef7;text-align:justify}
.intro__body p{margin-bottom:4px}
.intro__quote{position:absolute;left:160px;top:284px;width:150px;text-align:right;font-size:5.7px;line-height:1.45;color:var(--ink)}
.intro__quote .q{font-family:Georgia,serif;color:#8a98a8;font-size:11px;line-height:0}
.intro__author{position:absolute;right:14px;top:360px;color:var(--navy);font-size:8.4px;font-weight:600}

/* course */
.row{display:flex;gap:8px}
.row span:first-child{width:46px;flex:none}
.sub{font-weight:700;color:var(--navy);margin-top:3px}
.gauge-note{font-size:4.4px}

/* package */
.cols{display:flex;gap:8px}
.cols>div{flex:1}

/* footer */
.footer{position:absolute;left:0;bottom:0;width:100%;height:16px;background:var(--navy);color:#fff;font-family:"Marcellus SC",Georgia,serif;font-size:7px;text-align:right;padding:4px 10px 0 0}
</style>
</head>
<body>

<!-- PAGE 1 : COVER -->
<section class="page page--top cover">
  <svg class="abs" width="326" height="456" viewBox="0 0 326 456">
    <defs>
      <linearGradient id="coverSky" x1="0" y1="0" x2="1" y2="1">
        <stop offset="0" stop-color="#d9edf8"/><stop offset="1" stop-color="#6fb8e2"/>
      </linearGradient>
      <linearGradient id="coverBand" x1="0" y1="0" x2="0" y2="1">
        <stop offset="0" stop-color="#5aaee0"/><stop offset="1" stop-color="#9fd0ee"/>
      </linearGradient>
    </defs>
    <rect width="326" height="456" fill="url(#coverSky)"/>
    <polygon points="212,0 240,0 326,150 326,200" fill="url(#coverBand)" opacity=".9"/>
    <polygon points="0,456 0,367 230,367 120,456" fill="var(--navy)"/>
  </svg>
  <div class="photo" role="img" aria-label="Smiling medical receptionist in white coat with stethoscope holding a clipboard" style="left:0;top:0;width:326px;height:343px;background:linear-gradient(135deg,#f4f6f8 0%,#dfe7ee 45%,#b9c9d8 100%);clip-path:polygon(0 0,212px 0,326px 196px,326px 300px,222px 343px,0 343px)"></div>
  <div class="cover__band-text">BSB31115 Certificate III in Business Administration (Medical)</div>
  <div class="cover__name">Carrowmere Institute of Training</div>
  <div class="abs brand" style="left:230px;top:330px;font-size:7px;flex-direction:column;gap:2px;text-align:center;width:82px">
    <span>Carrowmere Institute<br>of Training</span><span class="brand__dot" style="width:16px;height:16px"></span>
  </div>
  <div class="cover__contact">
    <div>● www.carrowmeretraining.edu.au</div>
    <div class="phone">✆ 1800 555 014</div>
    <div style="padding-left:13px">(free call)</div>
  </div>
  <div class="cover__tag">Enriching Minds<br>Accelerating Careers</div>
</section>

<!-- PAGE 2 : INTRO -->
<section class="page page--top intro">
  <div class="abs" style="inset:0;background:linear-gradient(180deg,#eaf4fb,#ffffff 60%)"></div>
  <div class="intro__box"></div>
  <div class="intro__code"><div class="code">BSB31115<br>Certificate III</div>in<br>Business<br>Administration<br>(Medical)</div>
  <div class="intro__body tiny">
    <p>Gain the knowledge and skills to become a professional Medical Administrator by completing the Nationally Recognised Qualification in Business Administration (Medical). You will be employed in a variety of professional environments where your skills and contribution will be highly valued.</p>
    <p>This qualification is designed to give you the knowledge and skills required to become an integral part of the medical healthcare team. Find yourself in a role where you're appreciated by patients and your support is relied upon by the clinical team to keep the business administration running smoothly.</p>
    <p>Your efficient, diligent, caring approach makes a significant difference to the lives of others and engenders a sense of job satisfaction second to none.</p>
    <p>Medical Administration is a vibrant career with qualified administrators being widely sought after in industry – therefore career opportunities are strong. With an aging population, medical administration is a government recognised growth area with strong upwards projections of job opportunities predicted into 2020 and beyond.</p>
    <p>There are a variety of opportunities in diverse fields such as general practice, specialist practice, hospitals, dental and allied health. For students interested in career advancement, there are strong pathways to promotion available into more senior levels of administration and practice management.</p>
    <p>This course is ideal for those wanting to begin a career in the health professions and for workplace trainees. Mature aged students are also highly sought after in the medical space. Career opportunities are high for both part-time and full-time employees.</p>
  </div>
  <div class="photo" role="img" aria-label="Smiling student working on a laptop" style="left:0;top:282px;width:210px;height:174px;background:linear-gradient(120deg,#e9eef3,#c9d7e4 60%,#f5f7f9)"></div>
  <div class="intro__quote"><span class="q">“</span> The trainers were excellent in their delivery and knowledge. I want to say a huge thank you to Carrowmere for the course and knowledge I came away with. I have secured a fantastic job after my first application! Such good value for money too! I would highly recommend it. I'm a mature age person so it's never too late to up-skill yourself to get what you deserve! <span class="q">”</span></div>
  <div class="intro__author">- Jana Merritt</div>
  <div class="abs brand" style="left:236px;top:384px;font-size:6.4px;flex-direction:column;gap:3px;text-align:center;width:80px">
    <span>Carrowmere Institute<br>of Training</span><span class="brand__dot" style="width:22px;height:22px"></span>
  </div>
</section>

<!-- PAGE 3 : COURSE CONTENT -->
<section class="page page--bottom course">
  <div class="abs" style="left:0;top:0;width:245px;height:462px;background:linear-gradient(180deg,#e4f2fa,#f4fafd)"></div>
  <div class="photo" role="img" aria-label="Receptionists at a clinic front desk" style="left:246px;top:0;width:86px;height:72px;background:linear-gradient(135deg,#eef2f5,#c6d4e0)"></div>
  <div class="photo" role="img" aria-label="Medical team in white coats" style="left:246px;top:74px;width:86px;height:74px;background:linear-gradient(135deg,#f2f5f7,#c3d3e2)"></div>
  <div class="photo" role="img" aria-label="Administrator with folders in an office" style="left:246px;top:150px;width:86px;height:72px;background:linear-gradient(135deg,#e7ecf0,#b8c9d8)"></div>
  <div class="photo" role="img" aria-label="Doctors and nurses group" style="left:246px;top:224px;width:86px;height:76px;background:linear-gradient(135deg,#f1f4f6,#c8d6e2)"></div>

  <div class="hd" style="left:0;top:14px;width:108px">Course Content</div>
  <div class="abs tiny" style="left:14px;top:34px;width:226px">
    <div style="font-size:5.6px;margin-bottom:2px">Units of Competency Covered in the Carrowmere Programme :</div>
    <div class="sub">Core</div>
    <div class="row"><span>BSBITU307</span><span>Develop keyboarding speed and accuracy</span></div>
    <div class="row"><span>BSBWHS201</span><span>Contribute to health and safety of self and others</span></div>
    <div class="sub">Medical Skill Set</div>
    <div class="row"><span>BSBMED301</span><span>Interpret and apply medical terminology appropriately</span></div>
    <div class="row"><span>BSBMED302</span><span>Prepare and process medical accounts</span></div>
    <div class="row"><span>BSBMED303</span><span>Maintain patient records</span></div>
    <div class="row"><span>BSBMED305</span><span>Apply the principles of confidentiality, privacy and security within the medical environment</span></div>
    <div class="row"><span>BSBMED304</span><span>Assist in controlling stocks and supplies</span></div>
    <div class="sub">Business Administration (Medical) Skill Set including an introduction to Audio-typing</div>
    <div class="row"><span>BSBITU309</span><span>Produce desktop published documents</span></div>
    <div class="row"><span>BSBITU303</span><span>Design and produce text documents</span></div>
    <div class="row"><span>BSBITU306</span><span>Design and produce business documents</span></div>
    <div class="row"><span>BSBWRT301</span><span>Write simple documents</span></div>
    <div class="row"><span>BSBADM303</span><span>Produce texts from audio transcription</span></div>
    <div class="sub">Customer Service for Medical Administrators</div>
    <div class="row"><span>BSBCUS301</span><span>Deliver and monitor a service to customers</span></div>
    <div class="sub">Bonus training offered as part of the Carrowmere Programme</div>
    <ul class="tick">
      <li>Medical Triage for Non-Clinical Staff and Customer Service (BSBCUS301)</li>
      <li>CPR First Aid Qualification with National First Aid Council (BSBSXXXXX)</li>
      <li>OfficeDesk Write Essentials Short Course</li>
      <li>OfficeDesk Layout Essentials Short Course</li>
      <li>Carrowmere Typefast Online Keyboard Programme and certification to Australian Standards</li>
    </ul>
  </div>

  <div class="hd" style="left:0;top:314px;width:110px">Career Outcomes</div>
  <div class="abs tiny" style="left:12px;top:334px;width:232px">
    <div style="font-size:5.6px;margin-bottom:3px">Completing your Certificate III in Business Administration (Medical), you'll be qualified to work in the following areas :-</div>
    <div class="cols">
      <ul class="dots"><li>Medical Receptionist</li><li>Medical Secretary</li><li>Administration Assistant</li><li>Medical Administration</li><li>Ward Clerk</li></ul>
      <ul class="dots"><li>Medical Receptionist</li><li>Medical Accounts Clerk</li><li>Medical Records Administration</li><li>Front Desk Hospital Admissions</li></ul>
    </div>
    <div style="margin-top:8px;font-weight:700">Medical Receptionist<br>(ANZSCO code 542114)</div>
    <div>Expected job Opening</div>
  </div>
  <svg class="abs" style="left:80px;top:398px" width="100" height="52" viewBox="0 0 100 52">
    <path d="M8 48 A42 42 0 0 1 92 48 L70 48 A20 20 0 0 0 30 48 Z" fill="var(--navy)"/>
    <path d="M30 48 A20 20 0 0 1 70 48" fill="none" stroke="#fff" stroke-width=".6"/>
    <g stroke="#fff" stroke-width=".8"><line x1="50" y1="6" x2="50" y2="28"/><line x1="20" y1="18" x2="36" y2="34"/><line x1="80" y1="18" x2="64" y2="34"/><line x1="9" y1="36" x2="31" y2="42"/><line x1="91" y1="36" x2="69" y2="42"/></g>
    <text x="50" y="12" font-size="4" fill="#fff" text-anchor="middle">AVERAGE</text>
    <text x="18" y="46" font-size="4" fill="#fff">LOW</text>
    <text x="74" y="46" font-size="4" fill="#fff">HIGH</text>
  </svg>
  <div class="abs tiny" style="left:186px;top:410px;width:58px;font-size:4.2px">162,200 persons were employed as Receptionists in 2014, job openings over the next 5 years are expected to be greater than 50,000.</div>

  <div class="abs" style="left:252px;top:308px;width:76px;text-align:center;font-size:6px;color:var(--navy);font-weight:600">Industry Insights<div style="font-size:3.6px;font-weight:400">Demand Assistants</div></div>
  <svg class="abs" style="left:262px;top:326px" width="56" height="130" viewBox="0 0 56 130">
    <g fill="none" stroke="#cfdbe6" stroke-width="1"><circle cx="28" cy="18" r="16"/><circle cx="28" cy="62" r="16"/><circle cx="28" cy="106" r="16"/></g>
    <rect x="24" y="8" width="8" height="16" fill="var(--sky)"/>
    <g fill="var(--sky)"><rect x="19" y="60" width="3" height="10"/><rect x="23" y="56" width="3" height="14"/><rect x="27" y="63" width="3" height="7"/><rect x="31" y="65" width="3" height="5"/></g>
    <rect x="22" y="98" width="12" height="14" rx="2" fill="var(--navy)"/>
  </svg>
</section>

<!-- PAGE 4 : STUDY PACKAGE -->
<section class="page page--bottom package">
  <div class="abs" style="inset:0;background:linear-gradient(180deg,#e4f2fa,#eef7fc)"></div>
  <div class="hd hd--small" style="left:0;top:14px;width:228px">The Student Study Package – What You Receive</div>
  <div class="abs tiny" style="left:13px;top:31px;width:310px">
    <div style="font-size:5.4px;margin-bottom:3px">Students receive an array of helpful resources to keep as part of the Carrowmere Programme. These include :</div>
    <ul class="dots">
      <li>Carrowmere Institute Workbook <b>'Medical Receptionist and Secretary's Handbook'</b></li>
      <li>Carrowmere Institute Workbook <b>'Write, Design and Produce Documents for the Australian Medical Office'</b></li>
      <li>Carrowmere Institute Workbook <b>'Medical Triage and Customer Service for non-clinical staff'</b></li>
      <li><b>Access</b> to Carrowmere Online Learning platform</li>
      <li><b>Access</b> to Carrowmere Type-fast programme with testing and certification to Australian standards</li>
    </ul>
    <div class="cols">
      <ul class="dots">
        <li><b>OfficeDesk Write and Layout</b> online tutorials and certification</li>
        <li><b>Digital Medical Transcription Software</b> – student version.</li>
        <li><b>Medical Accounts Software ClinicLedger</b> – demo version to keep</li>
        <li><b>First Aid Council Basic First Aid Booklet and CPR Wallet Card</b></li>
        <li><b>Cardio Care Trust</b> endorsed online training programme</li>
      </ul>
      <ul class="dots">
        <li><b>CPR Accredited Training</b></li>
        <li><b>College endorsed Triage Guide Chart</b></li>
        <li><b>Access</b> to accredited specialist mentors and trainers</li>
        <li><b>Registration</b> into Carrowmere's Job-Network Club</li>
        <li><b>Cardio Care DVD</b> and Facts Pack for medical professionals</li>
      </ul>
    </div>
  </div>

  <div class="hd hd--small" style="left:0;top:150px;width:110px">Entry Requirements</div>
  <div class="abs tiny" style="left:13px;top:167px;width:310px">There are no formal entry requirements for this qualification, however it is recommended that individuals have a Year 10 standard of English and basic keyboard skills. Students with English as a second language may request a language, literacy and numeracy assessment during the enrolment and orientation session to determine learning support needs.</div>

  <div class="hd hd--small" style="left:0;top:194px;width:228px;line-height:1.1">Unique Delivery Model –<br>Combining Face-to-Face Learning with Self Paced</div>
  <div class="abs tiny" style="left:13px;top:219px;width:150px">
    <p>The Carrowmere Cert III Business Admin (Medical) Programme offers a unique structure to the medical administrative trainee - offering flexibility, intensive face-to-face training of crucial medical units combined with a self-paced home learning and a unique on-line learning programme. This allows studies to be undertaken at a convenient time by students and trainees.</p>
    <p style="margin-top:4px">The programme will adjust to differing skill levels and ability to commit time to the programme and can be completed in as little as 6 months to a maximum of 12 months – depending on prior experience and skills.</p>
    <div style="margin-top:5px;font-size:5.8px;font-weight:700;color:var(--navy)">Combined Assessment Approach<br>Duration : 6 – 12 months</div>
    <p style="margin-top:3px">Carrowmere utilise a variety of assessment processes which allow different learning styles to benefit from our programme. Assessment tools may include questioning, quizzes, assignments, projects, case studies and more. Workplace project work simulates real workplace activities utilising real medical forms, scripts, case histories, resources, practice software and reputable industry standards including the College of Practice Medicine, the Medical Standards Board, the First Aid Council and Cardio Care Trust.</p>
    <div style="margin-top:5px;font-size:5.8px;font-weight:700;color:var(--navy)">Student Support</div>
    <p>Students have direct access to a Trainer/Mentor for the duration of the programme and have direct access to Carrowmere Health Student On-Line Forum which students can engage with fellow students and trainers from across Australia.</p>
  </div>
  <div class="abs tiny" style="left:170px;top:219px;width:152px">
    <p>Carrowmere believe some units can only be taught effectively with face to face training led by industry experts and cannot be taught effectively by online learning alone. Therefore Carrowmere's Core Medical units are taught in workshop settings in 3 Saturdays (or through the week by prior arrangement) followed by self-paced and online delivery of core administration modules. The programme is further followed up with an intensive one day workshop.</p>
    <p style="margin-top:4px">For Traineeships, our Trainers physically attend site 1-2 times for personalised mentoring. There is a mentor/trainer assessor available at all times during our programme for all students.</p>
    <p style="margin-top:4px">All students are invited to Carrowmere's Computing Medical Software workshop day, where students work hands-on in a workplace simulated environment. Participants receive a complimentary demo copy of a Popular Medical software programme.</p>
  </div>
  <div class="photo" role="img" aria-label="Group of cheerful doctors and nurses giving thumbs up" style="left:186px;top:350px;width:146px;height:112px;background:linear-gradient(180deg,#eaf4fb 0%,#d5e2ec 50%,#bccddc 100%)"></div>
</section>

<!-- PAGE 5 : FUNDING & CONTACT -->
<section class="page page--bottom funding">
  <div class="abs" style="left:0;top:0;width:332px;height:185px;background:#ffffff"></div>
  <div class="hd hd--small" style="left:0;top:14px;width:128px">Funding (Queensland)</div>
  <div class="abs tiny" style="left:13px;top:30px;width:150px">
    <p>The Queensland Government will offset the cost of study for eligible students. You will still need to pay for a portion of your study costs.</p>
    <p style="margin-top:3px">Carrowmere Institute of Training has been chosen by the Department of Education and Training to deliver Government Subsidised Courses through the Certificate 3 Guarantee programme, VET Investment Plan and User Choice initiatives.</p>
  </div>
  <div class="abs tiny" style="left:170px;top:30px;width:150px">Therefore Carrowmere Institute are able to offer subsidised training for students who are eligible for the Certificate 3 Guarantee Programme, delivery and manage Traineeships in Cert III Business Administration (Medical) and offer services in Vocational Training for Schools (VETis). For Course and funding opportunities, please contact our office by email or phone to find out more.</div>

  <div class="hd hd--small" style="left:0;top:97px;width:128px">Certificate 3 Guarantee</div>
  <div class="abs tiny" style="left:13px;top:114px;width:240px">
    <p>You can receive a subsidy towards one certificate III qualification from a list of eligible courses. Give us a call to find out more.</p>
    <p style="margin-top:2px">You're eligible for the Certificate 3 Guarantee if you:</p>
  </div>
  <div class="abs tiny cols" style="left:20px;top:139px;width:300px">
    <ul class="tick"><li>Not hold or be currently undertaking a certificate III or higher level qualification. This does not include qualifications completed while at secondary school.</li><li>Be 15 years of age or older</li></ul>
    <ul class="tick"><li>Have finished secondary school or left school</li><li>Be an Australian citizen or permanent resident residing in Queensland, or New Zealand citizen permanently residing in Queensland.</li></ul>
  </div>
  <svg class="abs" style="left:268px;top:96px" width="56" height="44" viewBox="0 0 56 44"><circle cx="28" cy="20" r="17" fill="var(--sky)"/><rect x="6" y="24" width="44" height="9" fill="var(--navy)"/></svg>

  <div class="abs" style="left:0;top:185px;width:332px;height:277px;background:linear-gradient(180deg,#e4f2fa,#f3f9fd)"></div>
  <div class="photo" role="img" aria-label="Smiling doctors and nurses in a group" style="left:176px;top:185px;width:156px;height:120px;background:linear-gradient(135deg,#f1f4f7,#c5d5e3);clip-path:polygon(30% 0,100% 0,100% 100%,0 100%)"></div>
  <div class="abs" style="left:200px;top:185px;width:132px;height:3px;background:var(--sky)"></div>
  <div class="hd hd--small" style="left:0;top:189px;width:152px">Corporates and Traineeships</div>
  <div class="abs tiny" style="left:13px;top:206px;width:170px">Carrowmere offer a range of training opportunities to Corporates, Hospitals and Industry in either the full qualification or a range of individuals units, including <b>Patient Confidentiality, Medical Terminology, Medical Triage and Customer Service for Non-Clinical Staff.</b> For corporate enquiries, please email <span style="color:var(--sky)">info@carrowmeretraining.edu.au</span>. Great incentives are available for employers wanting to sponsor new staff to study the BSB31115 Business Administration (Medical) with bonus employer payments of between <b>$1500 - $5000</b>. Enquire today.</div>

  <div class="hd hd--small" style="left:0;top:266px;width:100px">Make an Enquiry</div>
  <div class="abs tiny" style="left:13px;top:283px;width:180px;font-size:5px">
    <p>Carrowmere's range of Medical Administration Training courses are designed to suit every budget and study situation. You may be eligible for Government subsidies for the Carrowmere Cert III Qualification where course costs are heavily discounted.</p>
    <p style="margin-top:4px">Enquiries : <b>info@carrowmeretraining.edu.au</b><br>or<br>FREECALL <b>1800 555 014</b></p>
  </div>
  <div class="photo" role="img" aria-label="Doctor with stethoscope smiling" style="left:196px;top:305px;width:136px;height:140px;background:linear-gradient(160deg,#f4f7f9,#ccdae6)"></div>

  <div class="abs" style="left:0;top:348px;width:332px;height:98px;background:#ffffff"></div>
  <div class="photo" role="img" aria-label="Smiling receptionist in white coat" style="left:100px;top:348px;width:60px;height:98px;background:linear-gradient(180deg,#eef2f6,#c9d6e2)"></div>
  <div class="abs" style="left:14px;top:358px;color:var(--sky);font-size:12px;font-weight:600">1800 555 014</div>
  <div class="abs" style="left:16px;top:374px;color:var(--navy);font-size:5.6px;font-weight:700;line-height:1.35">No matter your question,<br>we are here to help!</div>
  <div class="abs brand" style="left:16px;top:396px;font-size:4.8px;flex-direction:column;gap:2px;width:42px;text-align:center"><span>Carrowmere Institute of Training</span><span class="brand__dot" style="width:18px;height:18px"></span></div>
  <svg class="abs" style="left:170px;top:352px" width="156" height="24" viewBox="0 0 156 24">
    <g fill="#9aa7b4"><rect x="0" y="4" width="40" height="14" rx="2"/><circle cx="62" cy="11" r="7"/><rect x="80" y="4" width="34" height="14" rx="2"/><rect x="124" y="4" width="26" height="14" rx="2"/></g>
  </svg>
  <div class="abs tiny" style="left:170px;top:378px;width:156px;text-align:right;font-size:4.8px">Carrowmere Institute of Training details etc &nbsp;|&nbsp; RTO Reg 40187</div>
  <div class="abs" style="left:170px;top:393px;width:156px;text-align:right;font-size:5.8px;line-height:1.4;color:var(--navy)">Carrowmere Institute of Training<br>PO Box 410 Harlow Park DC<br>6051 <span style="color:var(--sky)">●</span><div style="margin-top:4px">info@carrowmeretraining.edu.au <span style="color:var(--sky)">✉</span></div></div>
  <div class="footer">www.carrowmeretraining.edu.au</div>
</section>

</body>
</html>
```